Nanny Share Ecommerce Website for Finding Childcare and Parents who need Childcare KindCribHelp.com

Our company needs an ecommerce website (KindCribHelp.com) for a US subscription based service strictly for nanny sharing that connects families and caregivers. The website would allow families to connect with one another as well as to search for nannies. The service would be searchable for other families by location (by radius or zip code), children demographic (age range/gender/special needs), days of week or times, after school care, school closure days (holidays), etc. The service would also be searchable for nannies based on gender, provider age range, years experience, language, hourly rate, transportation available, certification (CPR first aid), education etc. The search fields would be searchable and sortable and allow to connect with the provider (after paying subscription fee). The service would be similar to tendly.com in that it would allow for families and caregivers to post photos as well as a short bio of the themselves. There would also be a feedback/star rating mechanism to rate caregivers who have performed work for families (viewable to public). The service would be free for nannies to post their bios and only a subscription based service for families to connect with other families or with caregivers (able to view bio but need service to connect). There will be a short bio on the benefits of nanny sharing (reduced cost, increased flexibility for parents, reduced illness, increased socialization with other children vs. sole nanny), as well as Q&A section with best practices.

Target Market(s)

Families, Nannies

Industry/Entity Type

Childcare

Logo Text

Kind Crib Help

Coding

Coded - Design and coding required

Number of Pages Required

5+ page

Requirements
Must have
• Searchable (need to be able to search for families as well as nannies), responsive, functional, easy to use, add value to families and nannies. Needs to be able to collect payment for subscription.
Nice to have
• Optimized for mobile, SEO optimized

```html
<!DOCTYPE html>
<html lang="en">
<head>
<meta charset="utf-8">
<title>Kind Crib Help – Connects Families and Caregivers</title>
<link href="https://fonts.googleapis.com/css2?family=Montserrat:wght@400;500;600;700&family=Open+Sans:wght@400;600;700&display=swap" rel="stylesheet">
<style>
:root{
  --pink:#f5508c;
  --blue:#27b4ef;
  --ink:#2e2e2e;
  --text:#555;
  --muted:#888;
  --line:#e2e2e2;
  --field:#f7f7f7;
  --pale:#f4f4f4;
  --dark:#1f1f22;
  --white:#fff;
}
*{box-sizing:border-box;margin:0;padding:0}
html,body{width:1200px;height:4455px;overflow:hidden}
body{font-family:"Open Sans",Arial,sans-serif;color:var(--text);background:var(--white);position:relative;font-size:14px}
.abs{position:absolute}
h1,h2,h3,h4{font-family:"Montserrat",Arial,sans-serif;color:var(--ink)}

/* header */
.site-header{position:absolute;top:0;left:0;width:1200px;height:107px;display:flex;align-items:center;padding:0 100px;justify-content:space-between}
.brand{display:flex;align-items:center;gap:12px;font-family:"Montserrat",sans-serif;font-weight:700;font-size:25px;color:var(--ink)}
.brand-dot{width:30px;height:30px;border-radius:50%;background:var(--pink)}
.main-nav{display:flex;gap:38px;align-items:center;font-family:"Montserrat",sans-serif;font-size:15px;color:var(--ink)}
.main-nav .active{color:var(--blue)}

/* hero */
.hero{top:107px;left:0;width:1200px;height:548px;background:linear-gradient(100deg,#c9b9a8 0%,#e6d9cb 40%,#efe7dd 70%,#d9cfc4 100%)}
.hero-shade{position:absolute;inset:0;background:linear-gradient(180deg,rgba(0,0,0,.05),rgba(0,0,0,.25))}
.hero-title{position:absolute;top:280px;width:100%;text-align:center;color:var(--white);font-family:"Montserrat",sans-serif;font-weight:600;font-size:52px}
.hero-actions{position:absolute;top:365px;width:100%;display:flex;justify-content:center;gap:18px}
.btn{display:inline-flex;align-items:center;justify-content:center;border-radius:30px;font-family:"Montserrat",sans-serif;font-weight:600;font-size:14px;height:44px;padding:0 28px;text-transform:uppercase}
.btn-blue{background:var(--blue);color:var(--white)}
.btn-ghost{border:2px solid var(--white);color:var(--white)}
.slider-arrow{position:absolute;top:250px;width:40px;height:40px;border-radius:50%;background:rgba(0,0,0,.35);display:flex;align-items:center;justify-content:center}

/* search panel */
.search-panel{top:612px;left:100px;width:1000px;height:553px;background:var(--white);box-shadow:0 4px 22px rgba(0,0,0,.12);padding:50px 48px}
.panel-close{position:absolute;top:20px;right:22px;width:26px;height:26px;border-radius:50%;background:var(--blue);color:#fff;font-size:16px;display:flex;align-items:center;justify-content:center;font-weight:700}
.search-panel h3{font-size:27px;font-weight:600;margin-bottom:24px}
.form-row{display:flex;align-items:center;gap:16px;margin-bottom:26px;font-size:15px;color:var(--ink)}
.select,.input{height:34px;border:1px solid var(--line);background:var(--field);font-size:13px;color:#666;display:flex;align-items:center;padding:0 12px;justify-content:space-between}
.select::after{content:"";width:7px;height:7px;border-right:1.5px solid #777;border-bottom:1.5px solid #777;transform:rotate(45deg) translateY(-3px)}
.btn-refine{background:var(--pink);color:#fff;height:34px;width:205px;display:flex;align-items:center;justify-content:center;font-size:15px}

/* section titles */
.section-title{position:absolute;left:0;width:1200px;display:flex;align-items:center;justify-content:center;gap:30px;font-family:"Montserrat",sans-serif;font-size:40px;font-weight:400;color:var(--ink)}
.section-title::before,.section-title::after{content:"";width:190px;height:1px;background:var(--line)}
.section-title.light{color:#fff}
.section-title.light::before,.section-title.light::after{background:rgba(255,255,255,.45)}

/* services */
.service{width:250px;font-size:13px;line-height:1.75}
.service h4{font-size:19px;font-weight:600;margin-bottom:14px}
.service.left{text-align:right}
.btn-outline-pink{display:inline-flex;border:1.5px solid var(--pink);color:var(--pink);border-radius:20px;height:30px;padding:0 20px;align-items:center;font-size:12px;font-family:"Montserrat",sans-serif;margin-top:22px}
.photo-circle{border-radius:50%;border:6px solid #fff;box-shadow:0 4px 16px rgba(0,0,0,.15)}

/* benefits */
.benefits{top:1650px;left:0;width:1200px;height:430px;background:linear-gradient(200deg,#2ab5ef 0%,#6d87d4 45%,#c66aa7 75%,#f35a8c 100%)}
.benefit{position:absolute;top:155px;width:235px;text-align:center;color:#fff;font-size:13px;line-height:1.65}
.benefit h4{color:#fff;font-size:17px;font-weight:600;margin:12px 0 6px}
.benefit svg{display:block;margin:0 auto}

/* about */
.kicker{font-family:"Montserrat",sans-serif;color:var(--blue);font-size:16px}
.about h2{font-size:40px;font-weight:600;line-height:1.2;margin:8px 0 24px}
.about p{font-size:14px;line-height:1.9;color:var(--text)}

/* faq */
.faq{top:2697px;left:0;width:1200px;height:586px;background:var(--pale)}
.faq-list{position:absolute;top:178px;left:163px;width:874px}
.faq-item{background:#fff;border:1px solid var(--line);height:40px;display:flex;align-items:center;justify-content:space-between;padding:0 22px;font-size:14px;color:var(--ink);margin-bottom:15px}
.faq-item b{color:var(--pink);margin-right:8px}
.faq-open .faq-item{background:var(--pink);color:#fff;border-color:var(--pink);margin-bottom:0}
.faq-open .faq-item b{color:#fff}
.faq-answer{background:#fff;border:1px solid var(--line);border-top:0;padding:16px 22px;font-size:13px;line-height:1.85;margin-bottom:15px;color:var(--text)}
.gear{width:12px;height:12px;border-radius:50%;border:3px solid #999}

/* how */
.how{top:3283px;left:0;width:1200px;height:490px;background:linear-gradient(75deg,#f3528b 0%,#b45fae 45%,#5f8fd8 75%,#2ab5ef 100%)}
.step{position:absolute;top:210px;width:240px;text-align:center;color:#fff;font-family:"Montserrat",sans-serif;font-weight:600;font-size:17px;line-height:1.5}
.step-icon{width:108px;height:108px;border-radius:50%;background:#fff;border:6px solid rgba(255,255,255,.45);background-clip:padding-box;margin:0 auto 22px;display:flex;align-items:center;justify-content:center}
.step-link{position:absolute;top:264px;height:2px;border-top:2px dotted rgba(255,255,255,.8)}

/* testimonials */
.quote{position:absolute;top:3960px;width:470px;height:200px}
.avatar{position:absolute;left:0;top:0;width:98px;height:98px;border-radius:50%;border:4px solid #fff;box-shadow:0 0 0 2px var(--line)}
.quote p{position:absolute;left:125px;top:8px;width:330px;font-style:italic;font-size:13px;line-height:1.85;color:var(--muted)}
.quote .who{position:absolute;right:0;top:150px;text-align:right;font-family:"Montserrat",sans-serif;font-size:17px;color:var(--ink)}
.stars{display:flex;gap:3px;justify-content:flex-end;margin-top:4px}

/* footer */
.site-footer{top:4197px;left:0;width:1200px;height:258px;background:var(--dark);border-top:5px solid var(--blue);text-align:center}
.socials{position:absolute;top:78px;width:100%;display:flex;justify-content:center;gap:12px}
.socials span{width:36px;height:36px;border-radius:50%;border:1.5px solid #fff}
.foot-nav{position:absolute;top:140px;width:100%;display:flex;justify-content:center;gap:20px;color:#fff;font-size:14px}
.foot-nav i{font-style:normal;color:#888}
.copyright{position:absolute;top:182px;width:100%;color:#ddd;font-size:12px}
</style>
</head>
<body>

<header class="site-header">
  <div class="brand"><span class="brand-dot"></span>Kind Crib Help</div>
  <nav class="main-nav">
    <span class="active">Home</span><span>About us</span><span>Services</span><span>How it Works</span><span>FAQ</span><span>Blog</span><span>Contact us</span>
    <svg width="16" height="16" viewBox="0 0 16 16"><circle cx="6.5" cy="6.5" r="5" fill="none" stroke="var(--pink)" stroke-width="2"/><line x1="10.5" y1="10.5" x2="15" y2="15" stroke="var(--pink)" stroke-width="2"/></svg>
  </nav>
</header>

<section class="hero abs" role="img" aria-label="Photo of a mother and young daughter playing with toy blocks">
  <div class="hero-shade"></div>
  <div class="slider-arrow" style="left:20px"><svg width="12" height="14"><polyline points="8,2 3,7 8,12" fill="none" stroke="#fff" stroke-width="2"/></svg></div>
  <div class="slider-arrow" style="right:20px"><svg width="12" height="14"><polyline points="4,2 9,7 4,12" fill="none" stroke="#fff" stroke-width="2"/></svg></div>
  <h1 class="hero-title">Connects Families and Caregivers</h1>
  <div class="hero-actions"><span class="btn btn-blue">Find Families</span><span class="btn btn-ghost">Search for Nannies</span></div>
</section>

<form class="search-panel abs">
  <span class="panel-close">×</span>
  <h3>General Information</h3>
  <div class="form-row">Within <span class="select" style="width:145px">10 miles</span> of Zip Code <span class="input" style="width:70px">99233</span><span style="margin-left:18px">Provider Age</span><span class="select" style="width:110px">Any</span><span style="margin-left:14px">Gender</span><span class="select" style="width:110px">Any</span></div>
  <div class="form-row">Language <span class="select" style="width:115px">Any</span><span style="margin-left:16px">Hourly Rate</span><span class="select" style="width:115px">Any</span><span style="margin-left:16px">Last Login</span><span class="select" style="width:115px">Any</span></div>
  <div class="form-row">Education Type <span class="select" style="width:565px">Any</span></div>
  <div class="form-row">Search by Keyword <span class="input" style="width:535px"></span></div>
  <h3 style="margin-top:40px">Experience</h3>
  <div class="form-row">Years of Experience <span class="select" style="width:225px">Any</span><span style="margin-left:12px">Number of Children</span><span class="select" style="width:230px">Any</span></div>
  <div class="form-row">Experienced with <span class="select" style="width:500px">Any</span><span class="btn-refine">Refine Results</span></div>
</form>

<h2 class="section-title" style="top:1248px">Our Services</h2>
<div class="service left abs" style="top:1372px;left:105px">
  <h4>Matching families</h4>
  <p>We know that finding a family to share your caregiver is just as important as finding a nanny. That's why we</p>
  <span class="btn-outline-pink">READ MORE</span>
</div>
<div class="photo-circle abs" style="top:1352px;left:375px;width:200px;height:200px;background:radial-gradient(circle at 50% 40%,#e9c9ae,#9c8a7a)" role="img" aria-label="Photo of a smiling family of four"></div>
<div class="photo-circle abs" style="top:1352px;left:625px;width:200px;height:200px;background:radial-gradient(circle at 50% 40%,#e7d8cc,#8e7f74)" role="img" aria-label="Photo of parents and children reading together on a sofa"></div>
<div class="service abs" style="top:1372px;left:848px">
  <h4>Finding Caregivers</h4>
  <p>Once you've found the perfect family to share, we recommend you start your search for a nanny...</p>
  <span class="btn-outline-pink">READ MORE</span>
</div>

<section class="benefits abs">
  <h2 class="section-title light" style="top:95px">Our benefits</h2>
  <div class="benefit" style="left:104px">
    <svg width="40" height="56" viewBox="0 0 40 56"><text x="20" y="44" text-anchor="middle" font-size="48" fill="none" stroke="#fff" stroke-width="1.6" font-family="Montserrat">$</text></svg>
    <h4>Reduced cost</h4><p>We know that paying for childcare is expensive. We'll help you significantly reduce costs by spreading</p>
    <svg width="14" height="10"><polyline points="2,2 7,7 12,2" fill="none" stroke="#fff" stroke-width="2"/></svg>
  </div>
  <div class="benefit" style="left:349px">
    <svg width="70" height="56" viewBox="0 0 70 56" fill="none" stroke="#fff" stroke-width="1.6"><circle cx="22" cy="12" r="7"/><circle cx="48" cy="12" r="7"/><path d="M10 50V30a12 12 0 0 1 24 0v20M36 50V30a12 12 0 0 1 24 0v20"/></svg>
    <h4>Increased flexibility<br>for parents</h4><p>Worry no more... Do you work week-ends, evenings, or just need after</p>
    <svg width="14" height="10"><polyline points="2,2 7,7 12,2" fill="none" stroke="#fff" stroke-width="2"/></svg>
  </div>
  <div class="benefit" style="left:593px">
    <svg width="56" height="56" viewBox="0 0 56 56" fill="none" stroke="#fff" stroke-width="1.6"><circle cx="28" cy="14" r="8"/><path d="M14 50V34a14 14 0 0 1 28 0v16M22 34h12M28 28v12"/></svg>
    <h4>Reduced illness</h4><p>Did you know that daycare is an established risk factor for upper respiratory illness and ear infections,</p>
    <svg width="14" height="10"><polyline points="2,2 7,7 12,2" fill="none" stroke="#fff" stroke-width="2"/></svg>
  </div>
  <div class="benefit" style="left:838px">
    <svg width="70" height="56" viewBox="0 0 70 56" fill="none" stroke="#fff" stroke-width="1.6"><circle cx="18" cy="14" r="7"/><circle cx="50" cy="22" r="6"/><path d="M6 50V32a12 12 0 0 1 24 0v18M40 50V38a10 10 0 0 1 20 0v12M4 50h62"/></svg>
    <h4>Increased Socialization</h4><p>Social development is key in the early years of child development. Your child will have the opportunity</p>
    <svg width="14" height="10"><polyline points="2,2 7,7 12,2" fill="none" stroke="#fff" stroke-width="2"/></svg>
  </div>
</section>

<section class="about abs" style="top:2218px;left:100px;width:580px">
  <div class="kicker">Kind Crib Help</div>
  <h2>We Are More Than Just a<br>Nanny Agency</h2>
  <p>We are unique in that we truly help to match you with the perfect families to share care with. We understand the benefits of sharing in-home care with families that share your values and care-needs. Many families would prefer a personalized approach to childcare, but the significant burden of cost can deter many. Nanny sharing can significantly reduce costs to hiring a nanny alone.</p>
  <span class="btn btn-blue" style="margin-top:34px;text-transform:none;font-size:15px">Learn More</span>
</section>
<div class="abs" style="top:2170px;left:700px;width:500px;height:520px;background:linear-gradient(160deg,#f3ece4 0%,#e7d4c2 45%,#c9d84a 75%,#b5c93a 100%)" role="img" aria-label="Photo of a mother holding her baby on a green exercise ball"></div>

<section class="faq abs">
  <h2 class="section-title" style="top:98px">Frequently asked Questions</h2>
  <div class="faq-list">
    <div class="faq-open">
      <div class="faq-item"><span><b>Q.</b>What is Nanny Sharing?</span><span style="width:12px;height:12px;border-radius:50%;background:#fff"></span></div>
      <div class="faq-answer">Nanny share is typically when two or more families employ one nanny, sharing the cost of his or her salary. Most nannies watch all the children together, but many families work together to personalize schedules. Since both families are contributing to the nanny's pay, the nanny is usually able to earn more than working for a single family while also being a cost effective solution for the parents.</div>
    </div>
    <div class="faq-item"><span><b>Q.</b>Do I search for a Nanny or Family First?</span><span class="gear"></span></div>
    <div class="faq-item"><span><b>Q.</b>How do we determine the nanny's salary and benefits</span><span class="gear"></span></div>
    <div class="faq-item"><span><b>Q.</b>Do we need to withhold employment tax for the nanny share?</span><span class="gear"></span></div>
  </div>
</section>

<section class="how abs" aria-label="How it Works">
  <h2 class="section-title light" style="top:92px">How it Works</h2>
  <div class="step-link" style="left:268px;width:132px"></div>
  <div class="step-link" style="left:520px;width:127px"></div>
  <div class="step-link" style="left:767px;width:129px"></div>
  <div class="step" style="left:88px"><div class="step-icon"><svg width="40" height="40" viewBox="0 0 40 40" fill="var(--blue)"><circle cx="20" cy="13" r="8"/><path d="M5 38a15 15 0 0 1 30 0z"/></svg></div>Create a Profile<br>for Free</div>
  <div class="step" style="left:340px"><div class="step-icon"><svg width="40" height="40" viewBox="0 0 40 40" fill="none" stroke="var(--blue)" stroke-width="5"><circle cx="17" cy="17" r="11"/><line x1="25" y1="25" x2="36" y2="36"/></svg></div>Search for Families or<br>Nannies for Free</div>
  <div class="step" style="left:587px"><div class="step-icon"><svg width="40" height="40" viewBox="0 0 24 24" fill="var(--blue)"><path d="M6.6 10.8a15.1 15.1 0 0 0 6.6 6.6l2.2-2.2a1 1 0 0 1 1-.25 11.4 11.4 0 0 0 3.6.57 1 1 0 0 1 1 1V20a1 1 0 0 1-1 1A17 17 0 0 1 3 4a1 1 0 0 1 1-1h3.5a1 1 0 0 1 1 1c0 1.25.2 2.45.57 3.57a1 1 0 0 1-.25 1z"/></svg></div>Contact Families<br>and Caregivers</div>
  <div class="step" style="left:836px"><div class="step-icon"><svg width="42" height="40" viewBox="0 0 42 40" fill="none" stroke="var(--blue)" stroke-width="3"><path d="M6 16h26a13 13 0 0 1-26 0zM19 16V3a13 13 0 0 1 13 13M32 16l6-8"/><circle cx="12" cy="35" r="3"/><circle cx="28" cy="35" r="3"/></svg></div>Enjoy your<br>Personalized Childcare</div>
</section>

<h2 class="section-title" style="top:3868px">What Clients Say</h2>
<div class="quote" style="left:108px">
  <div class="avatar" style="background:linear-gradient(160deg,#d9cdc4,#8a7d76)" role="img" aria-label="Client portrait"></div>
  <p>Sharing a nanny with another family gave our son a best friend and cut our childcare bill in half this year.</p>
  <div class="who">~ Maren<div class="stars"><svg width="80" height="14" viewBox="0 0 80 14" fill="var(--blue)"><g id="s"><polygon points="7,0 9,5 14,5 10,8.5 11.5,14 7,10.5 2.5,14 4,8.5 0,5 5,5"/></g><use href="#s" x="16"/><use href="#s" x="32"/><use href="#s" x="48"/><use href="#s" x="64"/></svg></div></div>
</div>
<div class="quote" style="left:630px">
  <div class="avatar" style="background:linear-gradient(160deg,#d9cdc4,#8a7d76)" role="img" aria-label="Client portrait"></div>
  <p>We found a caring family nearby within a week, and our nanny loves the flexible schedule we share together.</p>
  <div class="who">~ Maren<div class="stars"><svg width="80" height="14" viewBox="0 0 80 14" fill="var(--pink)"><g id="t"><polygon points="7,0 9,5 14,5 10,8.5 11.5,14 7,10.5 2.5,14 4,8.5 0,5 5,5"/></g><use href="#t" x="16"/><use href="#t" x="32"/><use href="#t" x="48"/><use href="#t" x="64"/></svg></div></div>
</div>

<footer class="site-footer abs">
  <div class="socials"><span></span><span></span><span></span><span></span><span></span><span></span><span></span></div>
  <nav class="foot-nav"><span>Home</span><i>/</i><span>About us</span><i>/</i><span>Services</span><i>/</i><span>How it works</span><i>/</i><span>FAQ</span><i>/</i><span>Blog</span><i>/</i><span>Contact us</span></nav>
  <div class="copyright">© Copyright 2018 Kind Crib Help. All Rights Reserved</div>
</footer>

</body>
</html>
```